Institute for Hollow Relief at Annapolis
business card and stationary
Institute for Hollow Relief at Annapolis -
Creative Brief
Professional
Dominic T. Halloway, MD
472 Fenwick Court, Suite 208 Annapolis, MD 21409
dthalloway82@mailbright.example
www.wombrelief.example
Use new logo Comprehensive Gynecologic Care with Specialization in Chronic Pain Disorders and Minimally Invasive Surgery
Appointment Date and Time: Mon. _______ Tue _____ Wed ______ Thurs_______ Fri_______ _______ AM _______ PM

```html
<!DOCTYPE html>
<html lang="en">
<head>
<meta charset="utf-8">
<title>Institute for Hollow Relief at Annapolis – Business Card</title>
<link rel="stylesheet" href="https://fonts.googleapis.com/css2?family=Cabin:wght@400;600&display=swap">
<style>
  :root {
    --backdrop: #e9e6e2;
    --card: #ffffff;
    --orchid: #b0659f;
    --orchid-deep: #9a4f8a;
    --charcoal: #4a4a4c;
    --slate: #6b6b6e;
    --swoosh-grey: #5d5d60;
    --rule: #8a8a8c;
  }
  html, body {
    margin: 0;
    padding: 0;
    width: 1200px;
    height: 780px;
    overflow: hidden;
    background: var(--backdrop);
    font-family: "Cabin", sans-serif;
  }
  .business-card {
    position: absolute;
    left: 100px;
    top: 105px;
    width: 1000px;
    height: 570px;
    background: var(--card);
    border-radius: 26px;
    overflow: hidden;
    box-shadow: 0 6px 18px rgba(0,0,0,0.12);
  }
  .edge-swoosh {
    position: absolute;
    left: 0;
    top: 0;
    width: 1000px;
    height: 570px;
  }
  .brand {
    position: absolute;
    left: 215px;
    top: 80px;
    display: flex;
    align-items: center;
    gap: 28px;
  }
  .brand-dot {
    width: 120px;
    height: 120px;
    border-radius: 50%;
    background: var(--orchid);
    flex: none;
  }
  .brand-name {
    margin: 0;
    font-weight: 400;
    font-size: 40px;
    line-height: 1.05;
    text-transform: uppercase;
    color: var(--charcoal);
    letter-spacing: 0.5px;
    width: 440px;
  }
  .practitioner {
    position: absolute;
    left: 118px;
    top: 318px;
    width: 340px;
    text-align: right;
  }
  .practitioner-name {
    margin: 0 0 32px;
    font-weight: 600;
    font-size: 30px;
    color: var(--orchid);
  }
  .practice-address {
    margin: 0;
    font-style: normal;
    font-size: 20px;
    line-height: 1.45;
    color: var(--slate);
  }
  .divider {
    position: absolute;
    left: 478px;
    top: 312px;
    width: 1.5px;
    height: 150px;
    background: var(--rule);
  }
  .contact-list {
    position: absolute;
    left: 500px;
    top: 306px;
    margin: 0;
    padding: 0;
    list-style: none;
    font-size: 19px;
    color: var(--charcoal);
  }
  .contact-item {
    display: flex;
    align-items: center;
    gap: 12px;
    height: 38px;
  }
  .contact-icon {
    width: 20px;
    height: 20px;
    flex: none;
    fill: var(--orchid);
  }
</style>
</head>
<body>
  <article class="business-card">
    <svg class="edge-swoosh" viewBox="0 0 1000 570" aria-hidden="true">
      <path d="M0 175 C 40 300, 120 470, 250 570 L 0 570 Z" fill="var(--orchid)"/>
      <path d="M0 190 C 45 320, 110 465, 215 570 L 190 570 C 95 470, 35 330, 0 225 Z" fill="var(--swoosh-grey)"/>
      <path d="M0 225 C 35 330, 95 470, 190 570 L 175 570 C 85 480, 28 350, 0 260 Z" fill="var(--card)"/>
    </svg>

    <header class="brand">
      <span class="brand-dot"></span>
      <h1 class="brand-name">Institute for Hollow Relief at Annapolis</h1>
    </header>

    <section class="practitioner">
      <p class="practitioner-name">Dominic T. Halloway, MD</p>
      <address class="practice-address">472 Fenwick Court, Suite 208<br>Annapolis, MD 21409</address>
    </section>

    <div class="divider"></div>

    <ul class="contact-list">
      <li class="contact-item">
        <svg class="contact-icon" viewBox="0 0 24 24"><path d="M6.6 10.8a15.1 15.1 0 0 0 6.6 6.6l2.2-2.2c.3-.3.7-.4 1-.2 1.1.4 2.3.6 3.6.6.6 0 1 .4 1 1V20c0 .6-.4 1-1 1A17 17 0 0 1 3 4c0-.6.4-1 1-1h3.5c.6 0 1 .4 1 1 0 1.3.2 2.5.6 3.6.1.3 0 .7-.2 1z"/></svg>
        <span>1-855-555-0174</span>
      </li>
      <li class="contact-item">
        <svg class="contact-icon" viewBox="0 0 24 24"><path d="M6.6 10.8a15.1 15.1 0 0 0 6.6 6.6l2.2-2.2c.3-.3.7-.4 1-.2 1.1.4 2.3.6 3.6.6.6 0 1 .4 1 1V20c0 .6-.4 1-1 1A17 17 0 0 1 3 4c0-.6.4-1 1-1h3.5c.6 0 1 .4 1 1 0 1.3.2 2.5.6 3.6.1.3 0 .7-.2 1z"/></svg>
        <span>410-555-0182</span>
      </li>
      <li class="contact-item">
        <svg class="contact-icon" viewBox="0 0 24 24"><path d="M7 3h8l2 2v4H7z M4 10h16a1 1 0 0 1 1 1v8a1 1 0 0 1-1 1H4a1 1 0 0 1-1-1v-8a1 1 0 0 1 1-1z M7 16h10v2H7z" fill-rule="evenodd"/></svg>
        <span>410-555-0196</span>
      </li>
      <li class="contact-item">
        <svg class="contact-icon" viewBox="0 0 24 24"><path d="M12 2a10 10 0 1 0 5 18.7l-.9-1.7A8 8 0 1 1 20 12v1.2a1.8 1.8 0 0 1-3.6 0V7.5h-2v.9A5 5 0 1 0 15 16a3.8 3.8 0 0 0 7-2.8V12A10 10 0 0 0 12 2zm0 13a3 3 0 1 1 0-6 3 3 0 0 1 0 6z"/></svg>
        <span>dthalloway82@mailbright.example</span>
      </li>
    </ul>
  </article>
</body>
</html>
```